Admin Backend Redesign

We need a redesign for our backend which supoosed to make the backoffice look more modern!

I will add screenshots of the backoffice so you know what data will be shown in the Admin.

Have in mind that the users of this backend are Doctors. We need a clinical look, modern and sharp. The backoffice is responsive, have that in mind. We need the backoffice to look as professional as possible.

The theme used for the website is: http://velmora.quillstack-sample.com/

ON the main page of the backoffice, under every widget i need some space to write an explanation what the widget is about.

The color code used in our logo and website is #57aad4 combined with white.

We are open for ideas!
Updates

Project Deadline Extended
Reason: Designs are ok, but nothing innovative. Please use more modern designs!

Project Deadline Extended
Reason: Havent recieved a perfect design yet. Please read instructions carefully! Thank you

Project Deadline Extended
Reason: Hey everybody, sorry for the delay. We will decide in 3 days. If anyone wants to add a Design, that would be great.

Target Market(s)

Doctors, therapists

Industry/Entity Type

It Professional

Font styles to use
Sans Serif

Requirements
Must have
• Must look uptodate, modern, like new back offices look nowadays

```html
<!DOCTYPE html>
<html lang="de">
<head>
<meta charset="utf-8">
<title>Klino Rate – Dashboard</title>
<link rel="stylesheet" href="https://fonts.googleapis.com/css2?family=Open+Sans:ital,wght@0,400;0,600;0,700;1,400&display=swap">
<style>
:root{
  --brand:#3f8ad0;
  --brand-dark:#2f73b3;
  --green:#3dbd98;
  --green-dark:#2e9e7e;
  --red:#dc434f;
  --red-dark:#b8323d;
  --text:#333;
  --muted:#777;
  --line:#e2e2e2;
  --panel-head:#f3f3f7;
  --page:#fff;
  --yellow:#f3cd34;
  --sky:#b8e0f6;
  --pie-red:#dc3e3e;
  --pie-green:#3db54a;
  --purple:#9b30ff;
  --gold:#d4a017;
}
*{box-sizing:border-box;margin:0;padding:0}
html,body{width:780px;height:1200px;overflow:hidden}
body{font-family:"Open Sans",Arial,sans-serif;color:var(--text);background:var(--page);position:relative;font-size:10px}
.topbar{position:absolute;left:0;top:0;width:780px;height:40px;background:var(--brand)}
.brandname{position:absolute;left:14px;top:12px;color:#fff;font-weight:700;font-size:12px;letter-spacing:.2px;line-height:16px}
.menu-btn{position:absolute;left:117px;top:9px;width:22px;height:22px;border:1px solid rgba(255,255,255,.7);border-radius:50%}
.menu-btn i{position:absolute;left:6px;width:9px;height:1.5px;background:#fff}
.user-btn{position:absolute;right:14px;top:10px;width:20px;height:20px;border-radius:50%;background:var(--brand-dark)}
.user-btn:after{content:"";position:absolute;left:6px;top:8px;border:4px solid transparent;border-top-color:#fff}
.sidebar{position:absolute;left:0;top:40px;width:150px;height:1160px;border-right:1px solid var(--line);background:#fff}
.profile{height:58px;border-bottom:1px solid var(--line);position:relative}
.avatar{position:absolute;left:10px;top:9px;width:38px;height:38px;border-radius:50%;background:linear-gradient(135deg,#8fb9d8,#3f6f96);border:2px solid #3dbd98}
.profile .name{position:absolute;left:56px;top:15px;font-style:italic;font-size:11px}
.profile .role{position:absolute;left:56px;top:30px;font-style:italic;font-size:7px;color:var(--muted)}
.nav-label{font-size:7px;color:#aaa;font-style:italic;text-transform:uppercase;padding:10px 10px 8px}
.nav a{display:flex;align-items:center;gap:8px;height:29px;padding-left:12px;font-style:italic;font-size:9px;color:#444;text-decoration:none;border-bottom:1px solid var(--line)}
.nav a.active{background:var(--brand);color:#fff}
.nav svg{width:8px;height:8px}
.pagehead{position:absolute;left:150px;top:40px;width:630px;height:57px;border-bottom:1px solid var(--line)}
.pagehead .icon{position:absolute;left:12px;top:11px;width:34px;height:34px;background:#555;border-radius:2px}
.pagehead h1{position:absolute;left:54px;top:12px;font-size:12px;font-weight:700;text-transform:uppercase}
.crumbs{position:absolute;left:54px;top:28px;color:var(--muted);font-size:9px}
.tile{position:absolute;top:116px;width:286px;height:90px;color:#fff}
.tile.green{left:164px;background:var(--green)}
.tile.red{left:470px;background:var(--red)}
.tile h2{position:absolute;left:15px;top:14px;font-weight:400;font-size:26px;line-height:1}
.tile p{position:absolute;left:15px;top:46px;font-size:9px}
.tile .foot{position:absolute;left:0;bottom:0;width:100%;height:19px;padding:0 15px;display:flex;justify-content:space-between;align-items:center;font-size:9px}
.green .foot{background:var(--green-dark)}
.red .foot{background:var(--red-dark)}
.tile .glyph{position:absolute;right:12px;top:20px}
.panel{position:absolute;width:286px;border:1px solid #ddd;background:#fff}
.panel-head{height:22px;background:var(--panel-head);border-bottom:1px solid #ddd;display:flex;align-items:center;font-size:10px}
.panel-head .pi{width:22px;height:21px;border-right:1px solid #ddd;display:flex;align-items:center;justify-content:center;margin-right:8px}
.panel-body{padding:10px 15px;font-size:8.8px;line-height:1.55;color:#444}
.panel-body p{margin-bottom:7px}
.xs-btn{display:inline-block;margin-left:12px;background:var(--brand);color:#fff;font-style:italic;font-size:7.5px;padding:3px 6px;border-radius:2px}
.chart-body{padding:6px 6px 0}
.legend{position:absolute;font-size:7.5px;color:#666;line-height:15.5px}
.legend i{display:inline-block;width:10px;height:8px;margin-right:4px;vertical-align:-1px}
.table-panel{position:absolute;width:286px;border:1px solid #ddd;background:#fff}
.table-panel .bar{height:21px;background:var(--brand);color:#fff;font-size:9.5px;padding:4px 16px}
.search{margin:12px 12px 12px auto;width:110px;height:22px;border:1px solid #ccc;font-size:8px;color:#aaa;padding:5px 6px;display:flex;justify-content:space-between}
table{width:262px;margin:0 12px;border-collapse:collapse;font-size:8.5px}
th{text-align:left;font-weight:700;font-size:8.5px;padding:5px 0;border-top:1px solid var(--line);border-bottom:1px solid #bbb;white-space:nowrap}
th .s{color:#999;font-weight:400;float:right;padding-right:4px;font-size:7px}
td{padding:5px 0;border-bottom:1px solid var(--line);white-space:nowrap}
td.link{color:var(--brand-dark)}
.lvl{display:inline-block;width:34px;height:6px;background:#c9d6e3;position:relative;vertical-align:0}
.lvl b{position:absolute;left:0;top:0;height:6px;background:#2ed08a}
.stars{letter-spacing:1px;font-size:10px}
.tfoot{display:flex;justify-content:space-between;align-items:center;padding:10px 12px 12px;font-size:8px}
.pager{display:flex;border:1px solid #ccc;border-radius:2px}
.pager span{width:21px;height:20px;display:flex;align-items:center;justify-content:center;border-left:1px solid #ddd;color:var(--brand-dark);font-size:8.5px}
.pager span:first-child{border-left:0}
.pager span.on{background:#1e88d0;color:#fff}
.footer-rule{position:absolute;left:169px;top:1139px;width:28px;border-top:1px solid #333}
.footer{position:absolute;left:169px;top:1153px;font-size:8px}
</style>
</head>
<body>
<header class="topbar">
  <div class="brandname">KLINO RATE</div>
  <div class="menu-btn"><i style="top:7px"></i><i style="top:10px"></i><i style="top:13px"></i></div>
  <div class="user-btn"></div>
</header>

<aside class="sidebar">
  <div class="profile">
    <div class="avatar" role="img" aria-label="Profilfoto der Nutzerin"></div>
    <div class="name">Mara Velt</div>
    <div class="role">Beach Lover</div>
  </div>
  <div class="nav-label">Navigation</div>
  <nav class="nav">
    <a class="active" href="#"><svg viewBox="0 0 10 10"><path d="M5 0 10 5H8.5V10H6V7H4V10H1.5V5H0Z" fill="#fff"/></svg>Dashbord</a>
    <a href="#"><svg viewBox="0 0 10 10" fill="#3f8ad0"><circle cx="5" cy="3" r="2.5"/><path d="M0 10C0 6 10 6 10 10Z"/></svg>Mein Konto</a>
    <a href="#"><svg viewBox="0 0 10 10" fill="#3f8ad0"><circle cx="5" cy="3" r="2.5"/><path d="M0 10C0 6 10 6 10 10Z"/></svg>Patientenbewertungen</a>
  </nav>
</aside>

<section class="pagehead">
  <div class="icon"><svg width="34" height="34" viewBox="0 0 34 34"><path d="M17 8 27 17H24V26H19V20H15V26H10V17H7Z" fill="#fff"/></svg></div>
  <h1>Dashbord Page</h1>
  <div class="crumbs">Dashbord &nbsp;›&nbsp; Page title</div>
</section>

<div class="tile green">
  <h2>Profile</h2><p>Profile bearbeiten</p>
  <svg class="glyph" width="16" height="18" viewBox="0 0 16 18" fill="#fff"><circle cx="8" cy="5" r="4.5"/><path d="M0 18C0 10 16 10 16 18Z"/></svg>
  <div class="foot"><span>Weiter</span><span>➜</span></div>
</div>
<div class="tile red">
  <h2>Patienten</h2><p>Patienten verwaltent</p>
  <svg class="glyph" width="24" height="18" viewBox="0 0 24 18" fill="#fff"><circle cx="12" cy="4.5" r="4"/><path d="M5 18C5 10 19 10 19 18Z"/><circle cx="4.5" cy="6" r="3"/><path d="M0 15C0 10 8 10 8 14Z"/><circle cx="19.5" cy="6" r="3"/><path d="M16 14C16 10 24 10 24 15Z"/></svg>
  <div class="foot"><span>Alle Ansehen</span><span>➜</span></div>
</div>

<div class="panel" style="left:164px;top:226px;height:200px">
  <div class="panel-head"><span class="pi"><svg width="9" height="7" viewBox="0 0 9 7"><path d="M0 6 3 2 5 4 9 0" stroke="#777" fill="none"/></svg></span>trendo Trend fur</div>
  <div class="panel-body">
    <p>Lorem ipsum dolor sit amet: <span class="xs-btn">Extra Small Button</span></p>
    <p>Consectetur adipiscing elit. Morbi mollis nisi justo, ut imperdiet nisi mollis in. Pellentesque bibendum dignissim congue. Morbi vestibulum dui at dolor cursus sollicitudin. Pellentesque blandit purus vitae diam viverra, vel tincidunt dui sodales. Pellentesque at lobortis urna.</p>
    <p>Ut ultrices euismod hendrerit. Curabitur in consequat quam. Mauris bibendum augue metus, in luctus sem luctus sit amet.</p>
    <p>Morbi tincidunt malesuada metus id egestas. Vivamus eu rhon-cus odio, volutpat consectetur diam.</p>
  </div>
</div>

<div class="panel" style="left:470px;top:226px;height:200px">
  <div class="panel-head"><span class="pi"><svg width="9" height="8" viewBox="0 0 9 8"><path d="M0 0V8H9M1 6 4 3 6 5 9 1" stroke="#777" fill="none"/></svg></span>trendo Trend fur</div>
  <svg width="284" height="176" viewBox="0 0 284 176" font-size="6.5" fill="#666" font-family="Open Sans,Arial,sans-serif">
    <g stroke="#e5e5e5">
      <line x1="22" y1="46" x2="274" y2="46"/><line x1="22" y1="91" x2="274" y2="91"/><line x1="22" y1="136" x2="274" y2="136"/>
      <line x1="52" y1="11" x2="52" y2="146"/><line x1="86" y1="11" x2="86" y2="146"/><line x1="120" y1="11" x2="120" y2="146"/><line x1="154" y1="11" x2="154" y2="146"/><line x1="188" y1="11" x2="188" y2="146"/><line x1="222" y1="11" x2="222" y2="146"/><line x1="256" y1="11" x2="256" y2="146"/>
    </g>
    <rect x="22" y="11" width="252" height="135" fill="none" stroke="#444" stroke-width="1.3"/>
    <text x="12" y="14">15</text><text x="12" y="59">10</text><text x="15" y="104">5</text><text x="15" y="148">0</text>
    <text x="39" y="157">Oct 2012</text><text x="73" y="157">Jan 2013</text><text x="107" y="157">Apr 2013</text><text x="143" y="157">Jul 2013</text><text x="176" y="157">Oct 2013</text><text x="210" y="157">Jan 2014</text><text x="243" y="157">Apr 2014</text>
    <polyline fill="none" stroke="#e8c13e" stroke-width="1.3" points="22,146 148,146 150,64 154,60 158,63 161,50 163,17 165,23 167,40 170,36 172,55 175,50 178,70 181,64 184,72 188,66 192,74 196,68 200,73 205,70 210,75 216,72 222,76 228,72 234,75 240,73 246,74 252,72 258,73 264,68 270,70 274,67"/>
  </svg>
</div>

<div class="panel" style="left:164px;top:448px;height:200px">
  <div class="panel-head"><span class="pi"><svg width="9" height="7" viewBox="0 0 9 7" fill="#777"><rect x="0" y="4" width="2" height="3"/><rect x="3" y="1" width="2" height="6"/><rect x="6" y="3" width="2" height="4"/></svg></span>Pie 1</div>
  <div class="chart-body">
    <svg width="272" height="168" viewBox="0 0 272 168">
      <rect x="15" y="10" width="246" height="150" fill="#fafafa"/>
      <g transform="translate(21,5)">
        <path d="M80 80L80 13A67 67 0 1 1 74.2 146.7Z" fill="var(--yellow)"/>
        <path d="M80 80L74.2 146.7A67 67 0 0 1 25.1 118.5Z" fill="var(--sky)"/>
        <path d="M80 80L25.1 118.5A67 67 0 0 1 80 13Z" fill="var(--pie-red)"/>
      </g>
    </svg>
    <div class="legend" style="left:226px;top:40px"><div><i style="background:var(--yellow)"></i>Series1</div><div><i style="background:var(--sky)"></i>Series2</div><div><i style="background:var(--pie-red)"></i>Series3</div></div>
  </div>
</div>

<div class="panel" style="left:470px;top:448px;height:200px">
  <div class="panel-head"><span class="pi"><svg width="9" height="7" viewBox="0 0 9 7" fill="#777"><rect x="0" y="4" width="2" height="3"/><rect x="3" y="1" width="2" height="6"/><rect x="6" y="3" width="2" height="4"/></svg></span>Pie 2</div>
  <div class="chart-body">
    <svg width="272" height="168" viewBox="0 0 272 168">
      <rect x="15" y="10" width="246" height="150" fill="#fafafa"/>
      <g transform="translate(2,0)">
        <path d="M80 80L80 8A72 72 0 0 1 98.6 10.4Z" fill="var(--yellow)"/>
        <path d="M80 80L98.6 10.4A72 72 0 0 1 139 38.7Z" fill="var(--sky)"/>
        <path d="M80 80L139 38.7A72 72 0 0 1 67.5 150.9Z" fill="var(--pie-red)"/>
        <path d="M80 80L67.5 150.9A72 72 0 0 1 8.3 73.7Z" fill="var(--pie-green)"/>
        <path d="M80 80L8.3 73.7A72 72 0 0 1 80 8Z" fill="var(--purple)"/>
      </g>
    </svg>
    <div class="legend" style="left:222px;top:38px"><div><i style="background:var(--yellow)"></i>Series1</div><div><i style="background:var(--sky)"></i>Series2</div><div><i style="background:var(--pie-red)"></i>Series3</div><div><i style="background:var(--pie-green)"></i>Series4</div><div><i style="background:var(--purple)"></i>Series5</div><div><i style="background:var(--gold)"></i>Series6</div></div>
  </div>
</div>

<div class="table-panel" style="left:164px;top:667px">
  <div class="bar">Stat 1</div>
  <div class="search"><span>Search...</span><span>⌕</span></div>
  <table>
    <tr><th>Name<span class="s">▲</span></th><th>Position<span class="s">⇕</span></th><th>Start date<span class="s">⇕</span></th><th>Salary<span class="s">⇕</span></th></tr>
    <tr><td>Gerda</td><td>Chefin</td><td>1.11.2013</td><td>Salami</td></tr>
    <tr><td>Gerda</td><td>Chefin</td><td>1.11.2013</td><td>Salami</td></tr>
    <tr><td>Gerda</td><td>Chefin</td><td>1.11.2013</td><td>Salami</td></tr>
  </table>
  <div class="tfoot"><span>Showing 1 to 5 of 20 entries</span><div class="pager"><span>‹</span><span class="on">1</span><span>2</span><span>3</span><span>4</span><span>›</span></div></div>
</div>

<div class="table-panel" style="left:470px;top:667px">
  <div class="bar">Stat 2</div>
  <div class="search"><span>Search...</span><span>⌕</span></div>
  <table>
    <tr><th>Domain<span class="s">▲</span></th><th>Niveau<span class="s">⇕</span></th><th>Keyw.<span class="s">⇕</span></th><th>E Keyw.<span class="s">⇕</span></th></tr>
    <tr><td>praxis1.test</td><td><span class="lvl"><b style="width:7px"></b></span></td><td>Gemeinsame Keywords SE</td><td>Keywords</td></tr>
    <tr><td>praxis1.test</td><td><span class="lvl"><b style="width:12px"></b></span></td><td>Gemeinsame Keywords SE</td><td>Keywords</td></tr>
    <tr><td>praxis1.test</td><td><span class="lvl"><b style="width:20px"></b></span></td><td>Gemeinsame Keywords SE</td><td>Keywords</td></tr>
  </table>
  <div class="tfoot"><span>Showing 1 to 5 of 20 entries</span><div class="pager"><span>‹</span><span class="on">1</span><span>2</span><span>3</span><span>4</span><span>›</span></div></div>
</div>

<div class="table-panel" style="left:164px;top:888px">
  <div class="bar">Stat 1</div>
  <div class="search"><span>Search...</span><span>⌕</span></div>
  <table>
    <tr><th>Name<span class="s">▲</span></th><th>Profilseite<span class="s">⇕</span></th><th>Bewertung<span class="s">⇕</span></th></tr>
    <tr><td class="link">ciao!</td><td class="link">xyz ungelost</td><td class="stars">★★★★★</td></tr>
    <tr><td class="link">ciao!</td><td class="link">xyz ungelost</td><td class="stars">★★★★★</td></tr>
    <tr><td class="link">ciao!</td><td class="link">xyz ungelost</td><td class="stars">★★★★★</td></tr>
  </table>
  <div class="tfoot"><span>Showing 1 to 5 of 20 entries</span><div class="pager"><span>‹</span><span class="on">1</span><span>2</span><span>3</span><span>4</span><span>›</span></div></div>
</div>

<div class="footer-rule"></div>
<footer class="footer">2014 © domain name</footer>
</body>
</html>
```